Cash Flow Slide Design

Help Make Slide flow, QB Lantern to paying Down HELOC Then Bring in new Home Purchase and look amazing.
Font styles to use
Serif
Colors
EB3D1F
EC4F4E
F09395
F8D3D4
FCEDEE

```html
<!DOCTYPE html>
<html lang="en">
<head>
<meta charset="UTF-8">
<title>Wealth Builder Account</title>
<link href="https://fonts.googleapis.com/css2?family=Marcellus&family=Roboto:wght@400;500;700&display=swap" rel="stylesheet">
<style>
  :root {
    --red: #d7141a;
    --ink: #111111;
    --white: #ffffff;
    --checking-top: #02303b;
    --checking-mid: #2d6673;
    --checking-low: #b9e6ef;
    --life-top: #0a2a9e;
    --life-low: #1d3fd0;
    --heloc-top: #158a1e;
    --heloc-low: #7ee08a;
    --home-top: #0a8ef2;
    --home-low: #0f5fc8;
  }
  * { margin: 0; padding: 0; box-sizing: border-box; }
  html, body { width: 1200px; height: 675px; overflow: hidden; background: var(--white); }
  .slide { position: relative; width: 1200px; height: 675px; font-family: "Roboto", sans-serif; color: var(--ink); }

  .brand { position: absolute; left: 34px; top: 20px; display: flex; align-items: center; gap: 6px; }
  .brand-dot { width: 24px; height: 24px; border-radius: 50%; background: var(--red); }
  .brand-name { font-family: "Roboto", sans-serif; font-weight: 700; font-size: 21px; color: var(--ink); letter-spacing: 0.3px; }

  .title { position: absolute; left: 0; right: 0; top: 16px; text-align: center; font-family: "Marcellus", serif; font-size: 45px; font-weight: 400; letter-spacing: 0.5px; }
  .title-rule { position: absolute; left: 484px; width: 232px; top: 76px; height: 2px; background: var(--red); }
  .subtitle { position: absolute; left: 0; right: 0; top: 89px; text-align: center; font-size: 18px; font-weight: 400; }

  .flow-label { position: absolute; font-size: 16px; font-weight: 500; text-align: center; line-height: 23px; transform: translateX(-50%); white-space: nowrap; }
  .flow-arrow { position: absolute; width: 57px; height: 44px; }
  .flow-arrow path { fill: var(--red); }

  .pill { position: absolute; top: 219px; width: 209px; height: 426px; border-radius: 105px; overflow: hidden; box-shadow: 0 8px 18px rgba(0,0,0,0.18); color: var(--white); }
  .pill-checking { left: 127px; background: var(--checking-top); }
  .pill-life { left: 397px; background: linear-gradient(180deg, var(--life-top), var(--life-low)); }
  .pill-heloc { left: 667px; background: var(--heloc-top); }
  .pill-home { left: 937px; background: var(--home-top); }

  .pill-photo { position: absolute; left: 0; right: 0; bottom: 0; }
  .pill-checking .pill-photo { top: 180px; background: linear-gradient(180deg, var(--checking-top) 0%, var(--checking-mid) 35%, #6fa9b5 65%, var(--checking-low) 100%); }
  .pill-life .pill-photo { top: 190px; background: linear-gradient(180deg, rgba(40,80,220,0.0), rgba(20,50,190,0.55) 60%, rgba(10,35,150,0.7)); }
  .pill-heloc .pill-photo { top: 170px; background: linear-gradient(180deg, var(--heloc-top) 0%, #4fc55a 25%, var(--heloc-low) 55%, #2a9c34 100%); }
  .pill-home .pill-photo { top: 200px; background: linear-gradient(180deg, var(--home-top) 0%, #3aa0f0 35%, #7ec4f5 60%, var(--home-low) 100%); }

  .pill-icon { position: absolute; left: 57px; top: 26px; width: 95px; height: 95px; border-radius: 50%; background: var(--white); display: flex; align-items: center; justify-content: center; }
  .pill-icon svg { width: 62px; height: 62px; }

  .pill-title { position: absolute; left: 0; right: 0; top: 135px; text-align: center; font-family: "Marcellus", serif; font-size: 23px; line-height: 31px; letter-spacing: 0.6px; }
  .pill-rule { position: absolute; left: 72px; width: 66px; height: 1.5px; }
  .pill-checking .pill-rule { top: 174px; background: #2d5962; }
  .pill-life .pill-rule { top: 205px; background: var(--white); }
  .pill-heloc .pill-rule { top: 174px; background: #2fb43a; }
  .pill-home .pill-rule { top: 205px; background: #1fa83a; }

  .pill-points { position: absolute; left: 0; right: 0; top: 222px; list-style: none; text-align: center; font-size: 16px; font-weight: 500; line-height: 23.5px; }
  .pill-points li { margin-bottom: 14px; }
</style>
</head>
<body>
<div class="slide">
  <div class="brand"><span class="brand-dot"></span><span class="brand-name">KEYSTONE WEALTH</span></div>

  <h1 class="title">Wealth Builder Account</h1>
  <div class="title-rule"></div>
  <p class="subtitle">Offset Account: Permanent Life Insurance</p>

  <svg width="0" height="0" style="position:absolute">
    <defs>
      <path id="curve-arrow" d="M1 43 C1 26 12 14 33 13 V1 L56 21 L33 41 V29 C18 29 7 33 1 43 Z"/>
    </defs>
  </svg>

  <div class="flow-label" style="left:169px; top:117px;">Funds<br>Transfer</div>
  <svg class="flow-arrow" style="left:148px; top:167px;" viewBox="0 0 57 44"><use href="#curve-arrow"/></svg>

  <div class="flow-label" style="left:296px; top:114px;">Funds<br>Transfer</div>
  <svg class="flow-arrow" style="left:269px; top:167px;" viewBox="0 0 57 44"><use href="#curve-arrow"/></svg>

  <div class="flow-label" style="left:772px; top:134px;">FT</div>
  <svg class="flow-arrow" style="left:744px; top:167px;" viewBox="0 0 57 44"><use href="#curve-arrow"/></svg>

  <div class="flow-label" style="left:1042px; top:103px;">New Home<br>Purchase</div>
  <svg class="flow-arrow" style="left:1015px; top:164px;" viewBox="0 0 57 44"><use href="#curve-arrow"/></svg>

  <div class="flow-label" style="left:64px; top:334px;">Income</div>
  <svg class="flow-arrow" style="left:36px; top:369px;" viewBox="0 0 57 44"><use href="#curve-arrow"/></svg>

  <div class="flow-label" style="left:64px; top:448px;">Income</div>
  <svg class="flow-arrow" style="left:36px; top:482px;" viewBox="0 0 57 44"><use href="#curve-arrow"/></svg>

  <section class="pill pill-checking">
    <div class="pill-photo" role="img" aria-label="Photo of a magnifying glass over a small wooden house model"></div>
    <div class="pill-icon">
      <svg viewBox="0 0 64 64">
        <circle cx="32" cy="32" r="28" fill="none" stroke="#02303b" stroke-width="3" stroke-dasharray="4 2.5"/>
        <circle cx="32" cy="32" r="22" fill="#02303b"/>
        <path d="M22 33 L29 40 L43 25" fill="none" stroke="#fff" stroke-width="5" stroke-linecap="round" stroke-linejoin="round"/>
      </svg>
    </div>
    <h2 class="pill-title">CHECKING</h2>
    <div class="pill-rule"></div>
  </section>

  <section class="pill pill-life">
    <div class="pill-photo" role="img" aria-label="Photo of an umbrella sheltering a small wooden family"></div>
    <div class="pill-icon">
      <svg viewBox="0 0 64 64">
        <path d="M32 30 C20 22 18 12 25 9 C29 7 32 10 32 12 C32 10 35 7 39 9 C46 12 44 22 32 30 Z" fill="#0a2a9e"/>
        <path d="M30 13 h4 v4 h4 v4 h-4 v4 h-4 v-4 h-4 v-4 h4 z" fill="#fff"/>
        <path d="M8 20 L12 36 L22 46 V54 H28 V44 L20 34 L24 30 L16 26 L14 18 Z" fill="#0a2a9e"/>
        <path d="M56 20 L52 36 L42 46 V54 H36 V44 L44 34 L40 30 L48 26 L50 18 Z" fill="#0a2a9e"/>
      </svg>
    </div>
    <h2 class="pill-title">OA LIFE<br>INSURANCE</h2>
    <div class="pill-rule"></div>
    <ul class="pill-points">
      <li>Optimal Transfer Point</li>
      <li>Cash Value Continues<br>To Grow</li>
      <li>Can Never Lose<br>Principal</li>
      <li>Cash Value</li>
    </ul>
  </section>

  <section class="pill pill-heloc">
    <div class="pill-photo" role="img" aria-label="Photo of a happy couple holding the keys to their new home"></div>
    <div class="pill-icon">
      <svg viewBox="0 0 64 64">
        <circle cx="32" cy="32" r="13" fill="#158a1e"/>
        <text x="32" y="38" text-anchor="middle" font-family="Roboto, sans-serif" font-weight="700" font-size="17" fill="#fff">$</text>
        <path d="M14 40 A20 20 0 0 1 40 13" fill="none" stroke="#158a1e" stroke-width="5"/>
        <path d="M50 24 A20 20 0 0 1 24 51" fill="none" stroke="#158a1e" stroke-width="5"/>
        <path d="M44 4 L54 16 L46 18 Z" fill="#158a1e"/>
        <path d="M20 60 L10 48 L18 46 Z" fill="#158a1e"/>
      </svg>
    </div>
    <h2 class="pill-title">HELOC</h2>
    <div class="pill-rule"></div>
  </section>

  <section class="pill pill-home">
    <div class="pill-photo" role="img" aria-label="Photo of a small wooden house model on moss among ferns"></div>
    <div class="pill-icon">
      <svg viewBox="0 0 64 64">
        <path d="M6 32 L32 9 L58 32" fill="none" stroke="#0a8ef2" stroke-width="6" stroke-linecap="round" stroke-linejoin="round"/>
        <rect x="44" y="10" width="7" height="13" fill="#0a8ef2"/>
        <path d="M14 32 L32 17 L50 32 V56 H38 V42 H26 V56 H14 Z" fill="#0a8ef2"/>
      </svg>
    </div>
    <h2 class="pill-title">NEW HOME<br>PURCHASE</h2>
    <div class="pill-rule"></div>
  </section>
</div>
</body>
</html>
```